I am a new company with the latest technology in the concrete polishing business

We need a logo design for a new company out of Toronto, Canada. We polish residential, commercial and industrial concrete as well as different epoxy toppings.

Target Market(s)

How Owners with expendable incomes

Industry/Entity Type

Construction

Contact Information for Business Card

be able to see content rather easily

Colors
0355a3
fbed22
1b1b1b

Requirements
Must have
• simple and elegant

```html
<!DOCTYPE html>
<html lang="en">
<head>
<meta charset="utf-8">
<title>Slabline Finish – Business Card</title>
<link href="https://fonts.googleapis.com/css2?family=Ubuntu:wght@400;500;700&family=Arimo:wght@400&display=swap" rel="stylesheet">
<style>
  :root {
    --paper: #ffffff;
    --ink: #1b1b1b;
    --amber: #e9a52b;
    --amber-deep: #d88f1c;
    --night: #050505;
    --night-soft: #1e2226;
    --text-light: #f4f4f4;
    --muted: #d6d6d6;
    --rule: #8a8a8a;
  }
  * { margin: 0; padding: 0; box-sizing: border-box; }
  html, body {
    width: 1200px; height: 702px; overflow: hidden; background: var(--paper);
  }
  .card {
    position: relative; width: 1200px; height: 702px; overflow: hidden;
    background: var(--paper);
  }
  .brand-area {
    position: absolute; left: 0; top: 0; width: 1200px; height: 383px;
    background: var(--paper);
  }
  .brand-name {
    position: absolute; left: 150px; top: 150px; width: 650px;
    display: flex; align-items: center; gap: 22px;
    font-family: "Ubuntu", sans-serif; font-weight: 700; font-size: 78px;
    letter-spacing: -1px; color: var(--ink); white-space: nowrap;
  }
  .brand-square {
    width: 46px; height: 46px; background: var(--amber); flex: none;
  }
  .worker-figure {
    position: absolute; left: 808px; top: 84px; width: 270px; height: 188px;
    background: linear-gradient(180deg, #3a3a3a 0%, #111111 100%);
    border-radius: 6px;
  }
  .accent-band {
    position: absolute; left: 0; top: 383px; width: 1200px; height: 10px;
    background: linear-gradient(90deg, var(--amber-deep), var(--amber) 50%, var(--amber-deep));
  }
  .contact-area {
    position: absolute; left: 0; top: 393px; width: 1200px; height: 309px;
    background: radial-gradient(ellipse at 65% 25%, var(--night-soft) 0%, var(--night) 70%);
  }
  .person {
    position: absolute; right: 634px; top: 462px; text-align: right;
  }
  .person-name {
    font-family: "Ubuntu", sans-serif; font-weight: 500; font-size: 35px;
    color: var(--amber); line-height: 1.1;
  }
  .person-role {
    margin-top: 8px;
    font-family: "Ubuntu", sans-serif; font-weight: 400; font-size: 23px;
    color: var(--muted);
  }
  .divider {
    position: absolute; left: 606px; top: 422px; width: 2px; height: 214px;
    background: var(--rule);
  }
  .contact-list {
    position: absolute; left: 638px; top: 428px; list-style: none;
    font-family: "Arimo", sans-serif; font-size: 28px; color: var(--text-light);
  }
  .contact-item {
    display: flex; align-items: flex-start; height: 35.5px; line-height: 35.5px;
    white-space: nowrap;
  }
  .contact-icon {
    width: 34px; height: 28px; margin-right: 10px; margin-top: 3px; flex: none;
    fill: var(--amber);
  }
  .contact-icon.blank { visibility: hidden; }
</style>
</head>
<body>
<div class="card">
  <section class="brand-area">
    <div class="brand-name"><span class="brand-square"></span>Slabline Finish</div>
    <div class="worker-figure" role="img" aria-label="Silhouette of a worker pushing a concrete floor grinding machine"></div>
  </section>

  <div class="accent-band"></div>

  <section class="contact-area"></section>

  <div class="person">
    <p class="person-name">Daniel Arvani</p>
    <p class="person-role">Owner</p>
  </div>

  <div class="divider"></div>

  <ul class="contact-list">
    <li class="contact-item">
      <svg class="contact-icon" viewBox="0 0 34 28" aria-hidden="true">
        <path d="M8 2c2 0 3 3 4 6 .4 1.2-1.5 2.5-1.5 3.5 1 3 4 6 7 7 1 0 2.3-1.9 3.5-1.5 3 1 6 2 6 4 0 2-3 5-5 5C12 25 3 16 3 7c0-2 3-5 5-5z"/>
      </svg>
      <span>416-555-0142</span>
    </li>
    <li class="contact-item">
      <svg class="contact-icon" viewBox="0 0 34 28" aria-hidden="true">
        <path d="M2 8h30v18H2z"/>
        <path d="M2 8l15 10 15-10" fill="none" stroke="#050505" stroke-width="2"/>
      </svg>
      <span>info@slablinefinish.com</span>
    </li>
    <li class="contact-item">
      <svg class="contact-icon" viewBox="0 0 34 28" aria-hidden="true">
        <circle cx="17" cy="14" r="12"/>
        <g fill="none" stroke="#050505" stroke-width="1.6">
          <ellipse cx="17" cy="14" rx="5" ry="12"/>
          <path d="M5 14h24M7 8h20M7 20h20M17 2v24"/>
        </g>
      </svg>
      <span>www.slablinefinish.com</span>
    </li>
    <li class="contact-item">
      <svg class="contact-icon" viewBox="0 0 34 28" aria-hidden="true">
        <path d="M17 2L2 14h4v12h8v-8h6v8h8V14h4z"/>
      </svg>
      <span>24 Granite Way Unit 7</span>
    </li>
    <li class="contact-item">
      <svg class="contact-icon blank" viewBox="0 0 34 28" aria-hidden="true"></svg>
      <span>Brookvale Ontario</span>
    </li>
    <li class="contact-item">
      <svg class="contact-icon blank" viewBox="0 0 34 28" aria-hidden="true"></svg>
      <span>P3N 2B9</span>
    </li>
  </ul>
</div>
</body>
</html>
```